International Food Manufacturer in the need of a new business card and logo.

Our Company - Northgate Pantry Ltd.

Our Industry - Food and Drink

We are a Wild Harvested Food Distributor / Manufacturer. We service the following food sectors: Supermarkets, Hotels, Restaurants, Cafes, Catering and all people looking to eat healthy food products.

Slogan - Your trusted source for all things wholesome

Business card details -

48-52 Marlow Lane
Hatherby Green
London
EC9Z 4RT United Kingdom
Dennis Prowle
+44 7000 481736 - UK
+971 50 7739205 - UAE
+38 063 914 2758 - Ukraine
dennis@northgatepantry.example
www.northgatepantry.example

Goal - We are looking for a dynamic modern new look for our corporate image and a designer who can bring this new concept to our future food product designs. Please try to incorporate 3d hexagonal vector Imaging in your design concepts.

Target Market(s)

Industry/Entity Type

Food Service

Contact Information for Business Card

Northgate Pantry Ltd.
48-52 Marlow Lane
Hatherby Green
London
EC9Z 4RT United Kingdom
Dennis Prowle
+44 7000 481736 - UK
+971 50 7739205 - UAE

Font styles to use
Serif

Colors

Designer to choose colors to be used in the design.

Requirements
Must have
• Please read project description above.
Nice to have
Should not have

```html
<!DOCTYPE html>
<html lang="en">
<head>
<meta charset="utf-8">
<title>Northgate Pantry Ltd. – Business Card</title>
<link rel="stylesheet" href="https://fonts.googleapis.com/css2?family=Questrial&family=Montserrat:wght@700&family=Italianno&display=swap">
<style>
  :root {
    --card-white: #ffffff;
    --band-mist: #d3e0e3;
    --olive: #8e9a5c;
    --olive-light: #a3ae78;
    --ink: #1d1d1b;
    --sketch-light: #f1f1f1;
    --sketch-mid: #dcdcdc;
  }
  html, body {
    margin: 0;
    padding: 0;
    width: 1200px;
    height: 686px;
    overflow: hidden;
    background: var(--card-white);
  }
  .card {
    position: relative;
    width: 1200px;
    height: 686px;
    background: var(--card-white);
    font-family: "Questrial", "Century Gothic", sans-serif;
    color: var(--ink);
    overflow: hidden;
  }
  .produce-illustration {
    position: absolute;
    left: 366px;
    top: 0;
    width: 748px;
    height: 131px;
    background: linear-gradient(180deg, var(--sketch-mid) 0%, var(--sketch-light) 100%);
    border-radius: 0 0 40px 40px;
  }
  .brand-square {
    position: absolute;
    left: 110px;
    top: 98px;
    width: 148px;
    height: 148px;
    background: var(--olive-light);
  }
  .brand-name {
    position: absolute;
    left: 328px;
    top: 168px;
    margin: 0;
    font-family: "Questrial", "Century Gothic", sans-serif;
    font-weight: 400;
    font-size: 55px;
    line-height: 60px;
    letter-spacing: 2px;
    color: var(--olive);
    white-space: nowrap;
  }
  .tagline {
    position: absolute;
    left: 385px;
    top: 240px;
    margin: 0;
    font-family: "Italianno", cursive;
    font-size: 58px;
    line-height: 60px;
    color: var(--ink);
    white-space: nowrap;
  }
  .contact-band {
    position: absolute;
    left: 0;
    top: 346px;
    width: 1200px;
    height: 340px;
    background: var(--band-mist);
  }
  .address,
  .person {
    position: absolute;
    top: 362px;
    margin: 0;
    font-style: normal;
    font-size: 34px;
    line-height: 45.7px;
    white-space: nowrap;
  }
  .address {
    right: 638px;
    top: 408px;
    text-align: right;
  }
  .address .company {
    font-family: "Montserrat", sans-serif;
    font-weight: 700;
    font-size: 31px;
    color: var(--olive);
  }
  .person {
    left: 601px;
  }
  .person .person-name {
    font-family: "Montserrat", sans-serif;
    font-weight: 700;
    font-size: 32px;
    letter-spacing: 0.5px;
    text-transform: uppercase;
  }
  .line { display: block; }
</style>
</head>
<body>
  <main class="card">
    <div class="produce-illustration" role="img" aria-label="Pencil sketch of fresh vegetables: corn, broccoli, artichoke, lettuce, leeks, tomatoes and potatoes"></div>

    <div class="brand-square" aria-hidden="true"></div>
    <h1 class="brand-name">NORTHGATE PANTRY LTD.</h1>
    <p class="tagline">Your trusted source for all things wholesome</p>

    <section class="contact-band"></section>

    <address class="address">
      <span class="line company">Northgate Pantry Ltd.</span>
      <span class="line">48-52 Marlow Lane</span>
      <span class="line">Hatherby Green</span>
      <span class="line">London</span>
      <span class="line">EC9Z 4RT United Kingdom</span>
    </address>

    <address class="person">
      <span class="line person-name">Dennis Prowle</span>
      <span class="line">+44 7000 481736 - UK</span>
      <span class="line">+971 50 7739205 - UAE</span>
      <span class="line">+38 063 914 2758 - Ukraine</span>
      <span class="line">dennis@northgatepantry.example</span>
      <span class="line">www.northgatepantry.example</span>
    </address>
  </main>
</body>
</html>
```